Australian Software Consultancy needs new Business Card Design

Design Business Card based on existing design artefacts (attached). We are open to all designs. As its a 2 sided design and we thought it might be quite striking to have one side with a black background and te other side with a white background.

Target Market(s)

Financial Services mainly.

Industry/Entity Type

Business

Contact Information for Business Card

Name :
Position :
Email :

Requirements
Must have
• Funky design using our existing assets

```html
<!DOCTYPE html>
<html lang="en">
<head>
<meta charset="utf-8">
<title>Bright Logic – Business Card</title>
<link rel="stylesheet" href="https://fonts.googleapis.com/css2?family=Roboto:wght@400;500;700&display=swap">
<style>
  :root {
    --backdrop: #4a3c33;
    --card-white: #ffffff;
    --card-black: #101010;
    --ink: #111111;
    --brand-red: #e5232b;
    --text-grey: #444444;
    --rule-grey: #9a9a9a;
  }
  * { margin: 0; padding: 0; box-sizing: border-box; }
  html, body {
    width: 1200px;
    height: 1200px;
    overflow: hidden;
    background: var(--backdrop);
    font-family: "Roboto", Arial, sans-serif;
  }
  .canvas { position: relative; width: 1200px; height: 1200px; }
  .card {
    position: absolute;
    left: 214px;
    width: 772px;
    height: 440px;
  }
  .card-front { top: 150px; background: var(--card-white); }
  .card-back { top: 633px; background: var(--card-black); }

  .brand-name {
    position: absolute;
    left: 49px;
    top: 166px;
    font-weight: 700;
    font-size: 40px;
    letter-spacing: 1px;
    color: var(--ink);
    text-transform: uppercase;
    white-space: nowrap;
  }
  .divider {
    position: absolute;
    left: 388px;
    top: 150px;
    width: 2px;
    height: 146px;
    background: var(--rule-grey);
  }
  .contact-block { position: absolute; left: 424px; top: 140px; }
  .person-name {
    font-weight: 500;
    font-size: 28px;
    color: var(--ink);
    line-height: 34px;
  }
  .person-role {
    font-size: 20px;
    color: var(--brand-red);
    line-height: 26px;
    margin-bottom: 20px;
  }
  .contact-list { list-style: none; }
  .contact-item {
    display: flex;
    align-items: center;
    gap: 7px;
    font-size: 18.5px;
    color: var(--text-grey);
    line-height: 27.5px;
  }
  .contact-icon { width: 17px; height: 17px; flex: none; }

  .back-mark {
    position: absolute;
    left: 0; right: 0; top: 0; bottom: 0;
    display: flex;
    align-items: center;
    justify-content: center;
    gap: 16px;
  }
  .back-dot {
    width: 34px; height: 34px;
    border-radius: 50%;
    background: var(--brand-red);
  }
  .back-name {
    font-weight: 700;
    font-size: 46px;
    letter-spacing: 1px;
    color: var(--brand-red);
    text-transform: uppercase;
  }
</style>
</head>
<body>
<main class="canvas">
  <section class="card card-front">
    <div class="brand-name">Bright Logic</div>
    <div class="divider"></div>
    <div class="contact-block">
      <div class="person-name">Marcus Reilly</div>
      <div class="person-role">President &amp; CEO</div>
      <ul class="contact-list">
        <li class="contact-item">
          <svg class="contact-icon" viewBox="0 0 24 24" fill="none" stroke="#e5232b" stroke-width="1.8" stroke-linejoin="round"><path d="M5 3h4l2 5-2.5 1.5a11 11 0 0 0 6 6L16 13l5 2v4a2 2 0 0 1-2 2A16 16 0 0 1 3 5a2 2 0 0 1 2-2z"/></svg>
          <span>000-111-2222</span>
        </li>
        <li class="contact-item">
          <svg class="contact-icon" viewBox="0 0 24 24" fill="none" stroke="#e5232b" stroke-width="1.8"><rect x="2.5" y="5" width="19" height="14" rx="1"/><path d="M3 6l9 7 9-7"/></svg>
          <span>mreilly@brightlogic-demo.com</span>
        </li>
        <li class="contact-item">
          <svg class="contact-icon" viewBox="0 0 24 24" fill="none" stroke="#e5232b" stroke-width="1.6"><circle cx="12" cy="12" r="9.5"/><ellipse cx="12" cy="12" rx="4" ry="9.5"/><path d="M2.5 12h19M4 7h16M4 17h16"/></svg>
          <span>www.brightlogic-demo.com</span>
        </li>
      </ul>
    </div>
  </section>

  <section class="card card-back">
    <div class="back-mark">
      <div class="back-dot"></div>
      <div class="back-name">Bright Logic</div>
    </div>
  </section>
</main>
</body>
</html>
```